Larkwell Bend responsive web design

We need a responsive, bootstrap compatible (but design only - PSD files) website design for a fly fishing shop and guide service.

Design should be very clean. Home Page design + interior page design please.

Possible Home Page Content:
Slide Show
Highlight Three Features: Guided Trips, Fly Shop, Missouri River
About

Thank you and good luck!

Industry/Entity Type

Shop

Requirements
Must have
• This will be used on Bootstrap CMS so needs 12 column bootstrap measurements.

DESIGN ONLY NEEDED (clean PSD files), no programming required.
Need a Home Page layout and secondary page layout

Must show use of the following:
H1 - H5 font uses
link color
Dropdown for navigation bar
Button example
Should not have
• No cutout images, this will be part of CMS and client needs to be able to update most content without knowing photoshop.

```html
<!DOCTYPE html>
<html lang="en">
<head>
<meta charset="utf-8">
<title>Larkwell Bend</title>
<link href="https://fonts.googleapis.com/css2?family=Open+Sans:wght@400;600;700&family=Raleway:wght@300;400;600&display=swap" rel="stylesheet">
<style>
:root{
  --blue:#0a8fd6;
  --sky:#6ecff6;
  --ink:#222;
  --text:#555;
  --muted:#777;
  --panel:#f3f3f3;
  --footer:#222;
  --footer-base:#141414;
  --line:#e05a4a;
  --white:#fff;
}
*{box-sizing:border-box;margin:0;padding:0}
html,body{width:735px;height:1200px;overflow:hidden;background:var(--white)}
body{position:relative;font-family:"Open Sans",Arial,sans-serif;color:var(--text)}
h1,h2,h3,h4{font-weight:400}
.abs{position:absolute}

/* header */
.brand{left:66px;top:36px;display:flex;align-items:center;gap:8px}
.brand-mark{width:22px;height:22px;background:var(--sky)}
.brand-name{font-weight:700;font-size:22px;color:var(--ink)}
.search{left:482px;top:30px;width:186px;height:22px;display:flex}
.search-field{flex:1;background:#f2f2f2;border:1px solid #e2e2e2;font-size:7px;color:#888;padding:6px 9px}
.search-btn{width:24px;background:var(--blue);display:flex;align-items:center;justify-content:center}
.nav{top:77px;left:317px;display:flex;font-size:9.5px;color:var(--ink)}
.nav a{color:var(--ink);text-decoration:none;margin-right:26px}
.nav a:last-child{margin-right:0}

/* hero */
.hero{left:0;top:106px;width:735px;height:338px;
  background:
    radial-gradient(ellipse 260px 90px at 560px 210px,rgba(60,70,140,.55),rgba(60,70,140,0)),
    radial-gradient(ellipse 300px 60px at 600px 120px,rgba(240,150,150,.55),rgba(240,150,150,0)),
    linear-gradient(180deg,#5d6fb0 0%,#8d86bf 18%,#c596b5 34%,#e9a4a0 46%,#f1c9b8 54%,#5f6c8e 56%,#c9c3d4 62%,#e6c7cc 78%,#d0c8d8 100%)}
.hero-box{left:58px;top:187px;width:327px;height:163px;background:rgba(20,20,20,.88);border-radius:2px;padding:18px 10px}
.hero-title{font-family:"Raleway",sans-serif;font-weight:300;font-size:34px;color:#fff;line-height:1}
.hero-title b{font-weight:600}
.hero-text{font-family:"Raleway",sans-serif;font-size:15.5px;color:#fff;line-height:1.2;margin:12px 0 0 4px}
.btn-primary{left:70px;top:301px;width:143px;height:30px;background:var(--blue);color:#fff;font-family:"Raleway",sans-serif;font-size:13px;display:flex;align-items:center;justify-content:center;border-radius:2px}

/* feature cards */
.card{top:420px;width:166px;height:106px;text-align:center;background:var(--white)}
.card-bar{width:46px;height:4px;background:var(--sky);margin:18px auto 10px}
.card-title{font-size:11.5px;font-weight:400;color:#333;margin-top:2px}
.card-sub{font-size:9px;color:var(--muted);margin-top:5px}
.card-photo{top:527px;width:167px;height:147px}

/* callout */
.callout{left:68px;top:710px;width:600px;height:69px;background:var(--panel);border-left:4px solid var(--sky)}
.callout-title{left:103px;top:719px;font-size:12.5px;color:var(--ink)}
.callout-text{left:103px;top:739px;width:445px;font-size:9.4px;line-height:1.25;color:#444}
.btn-discover{left:558px;top:737px;width:85px;height:24px;background:var(--blue);color:#fff;font-size:9.5px;display:flex;align-items:center;justify-content:center;border-radius:2px;box-shadow:0 1px 2px rgba(0,0,0,.3)}

/* services */
.services-title{left:95px;top:822px;font-family:"Raleway",sans-serif;font-weight:300;font-size:22.5px;color:var(--ink)}
.services-icon{left:63px;top:829px}
.services-text{left:86px;top:863px;width:285px;font-family:"Raleway",sans-serif;font-size:8.6px;line-height:1.55;color:#555}
.checks{left:86px;top:898px;width:290px;display:grid;grid-template-columns:147px 140px;row-gap:8px;font-family:"Raleway",sans-serif;font-size:8.6px;color:#555}
.checks span{display:flex;align-items:center;gap:4px}
.services-photo{left:389px;top:858px;width:133px;height:131px;background:linear-gradient(180deg,#a9c6a0 0%,#4f7d3a 14%,#3f6a2e 38%,#6f8f5a 50%,#55775a 62%,#3e5c4a 82%,#2f4a3a 100%);border:2px solid #fff;box-shadow:0 1px 4px rgba(0,0,0,.35)}
.connectors{left:522px;top:840px}
.thumb{width:58px;height:58px;border-radius:50%;border:2px solid #fff;box-shadow:0 1px 4px rgba(0,0,0,.3)}

/* footer */
.footer{left:0;top:1022px;width:735px;height:152px;background:var(--footer)}
.footer-base{left:0;top:1174px;width:735px;height:26px;background:var(--footer-base);color:#ddd;font-size:7.5px;display:flex;align-items:center;justify-content:center}
.footer-base b{font-weight:700;color:#fff;margin:0 2px}
.footer-head{font-size:15px;font-weight:700;color:#fff;display:flex;align-items:center;gap:8px}
.footer-links{left:77px;top:1070px;list-style:none;font-size:7.6px;line-height:11.7px}
.footer-links a{color:#fff;text-decoration:none}
.footer-links .active a{color:var(--sky)}
.footer-about{left:262px;top:1066px;width:145px;font-size:7.8px;line-height:11.7px;color:#fff}
.socials{left:264px;top:1130px;display:flex;gap:4px}
.socials span{width:15px;height:15px;border-radius:2px;background:var(--sky)}
.map{left:490px;top:1071px;width:148px;height:80px;background:linear-gradient(135deg,#ecebe5,#dcd9cf);border:2px solid #fff}
</style>
</head>
<body>

<header>
  <div class="abs brand"><span class="brand-mark"></span><span class="brand-name">Larkwell Bend</span></div>
  <div class="abs search">
    <div class="search-field">Search entire store here...</div>
    <div class="search-btn">
      <svg width="10" height="10" viewBox="0 0 10 10"><circle cx="4" cy="4" r="3" fill="none" stroke="#fff" stroke-width="1.4"/><line x1="6.2" y1="6.2" x2="9" y2="9" stroke="#fff" stroke-width="1.4"/></svg>
    </div>
  </div>
  <nav class="abs nav"><a href="#">HOME</a><a href="#">FLY SHOP</a><a href="#">GUIDE SERVICE</a><a href="#">MISSOURI RIVER</a><a href="#">CONTACT</a></nav>
</header>

<section>
  <div class="abs hero" role="img" aria-label="Fishing boat resting on a calm lake at sunset"></div>
  <div class="abs hero-box">
    <h1 class="hero-title">Larkwell <b>Bend</b></h1>
    <p class="hero-text">Lorem ipsum dolor sit amet, consecttetur adipisicing elit, sed do eiusmod tempor</p>
  </div>
  <a class="abs btn-primary">Read More</a>
</section>

<section>
  <div class="abs card" style="left:66px">
    <div class="card-bar"></div>
    <svg width="30" height="26" viewBox="0 0 30 26"><rect x="3" y="5" width="24" height="18" rx="3" fill="none" stroke="var(--blue)" stroke-width="2"/><path d="M8 19 L14 9 L20 19Z" fill="var(--blue)"/><rect x="10" y="2" width="10" height="4" fill="var(--blue)"/></svg>
    <h3 class="card-title">Guided Trips</h3>
    <p class="card-sub">Lorem Ipsum is simply</p>
  </div>
  <div class="abs card" style="left:274px">
    <div class="card-bar"></div>
    <svg width="30" height="26" viewBox="0 0 30 26"><rect x="3" y="2" width="24" height="7" fill="var(--blue)"/><rect x="5" y="10" width="20" height="14" fill="none" stroke="var(--blue)" stroke-width="2.5"/><rect x="8" y="13" width="7" height="5" fill="var(--blue)"/></svg>
    <h3 class="card-title">Fly Shop</h3>
    <p class="card-sub">Lorem Ipsum is simply</p>
  </div>
  <div class="abs card" style="left:501px">
    <div class="card-bar"></div>
    <svg width="30" height="26" viewBox="0 0 30 26"><path d="M13 2 L24 11 L13 14Z" fill="var(--blue)"/><rect x="12" y="2" width="2" height="16" fill="var(--blue)"/><path d="M3 18 H27 L23 23 H7Z" fill="var(--blue)"/></svg>
    <h3 class="card-title">Missouri River</h3>
    <p class="card-sub">Lorem Ipsum is simply</p>
  </div>

  <svg class="abs card-photo" style="left:66px" viewBox="0 0 167 147" role="img" aria-label="Two anglers in a drift boat on the river">
    <defs><linearGradient id="g1" x1="0" y1="0" x2="0" y2="1"><stop offset="0" stop-color="#a9b2bf"/><stop offset=".3" stop-color="#8a7f68"/><stop offset=".55" stop-color="#5f6a74"/><stop offset="1" stop-color="#3a4048"/></linearGradient></defs>
    <polygon points="0,38 83.5,0 167,38 167,147 0,147" fill="url(#g1)"/></svg>
  <svg class="abs card-photo" style="left:273px" viewBox="0 0 167 147" role="img" aria-label="Wooded riverbank reflected in the water">
    <defs><linearGradient id="g2" x1="0" y1="0" x2="0" y2="1"><stop offset="0" stop-color="#c9d6e6"/><stop offset=".3" stop-color="#6f7d55"/><stop offset=".6" stop-color="#a48a5e"/><stop offset=".7" stop-color="#5c6d7a"/><stop offset="1" stop-color="#3d4a55"/></linearGradient></defs>
    <polygon points="0,38 83.5,0 167,38 167,147 0,147" fill="url(#g2)"/></svg>
  <svg class="abs card-photo" style="left:501px" viewBox="0 0 167 147" role="img" aria-label="River under an evening sky">
    <defs><linearGradient id="g3" x1="0" y1="0" x2="0" y2="1"><stop offset="0" stop-color="#8fb0d8"/><stop offset=".3" stop-color="#e0c99a"/><stop offset=".5" stop-color="#a56a2c"/><stop offset=".65" stop-color="#c98a3a"/><stop offset="1" stop-color="#3c4a66"/></linearGradient></defs>
    <polygon points="0,38 83.5,0 167,38 167,147 0,147" fill="url(#g3)"/></svg>
</section>

<section>
  <div class="abs callout"></div>
  <h4 class="abs callout-title">Larkwell Bend</h4>
  <p class="abs callout-text">Lorem ipsum dolor sit amet, consectetur adipisicing elit, sed do eiusmod tempor incididunt ut labore et dolore magna aliqua. Ut enim ad minim veniam, quis nostrud exercitation ullamco laboris nisi ut</p>
  <a class="abs btn-discover">Discover more</a>
</section>

<section>
  <svg class="abs services-icon" width="28" height="14" viewBox="0 0 28 14"><path d="M1 7 C8 1 18 1 27 4 M3 9 C10 4 19 5 27 8 M6 11 C12 8 20 9 26 12" fill="none" stroke="var(--sky)" stroke-width="1.2"/></svg>
  <h2 class="abs services-title">Features Services</h2>
  <p class="abs services-text">Autem vel eum iriure dolor in hendrerit in vulputate velit esse molestie consequat, vel sequitur mutationem illum dolore eu feugiat nulla.</p>
  <div class="abs checks">
    <span><svg width="9" height="8" viewBox="0 0 9 8"><path d="M1 4 L3.5 6.5 L8 1" fill="none" stroke="#999" stroke-width="1.6"/></svg>Easy to use lorem interface</span>
    <span><svg width="9" height="8" viewBox="0 0 9 8"><path d="M1 4 L3.5 6.5 L8 1" fill="none" stroke="#999" stroke-width="1.6"/></svg>24x7 support on sit amet</span>
    <span><svg width="9" height="8" viewBox="0 0 9 8"><path d="M1 4 L3.5 6.5 L8 1" fill="none" stroke="#999" stroke-width="1.6"/></svg>Cost effective ipsum amet</span>
    <span><svg width="9" height="8" viewBox="0 0 9 8"><path d="M1 4 L3.5 6.5 L8 1" fill="none" stroke="#999" stroke-width="1.6"/></svg>Instant updation sit</span>
    <span><svg width="9" height="8" viewBox="0 0 9 8"><path d="M1 4 L3.5 6.5 L8 1" fill="none" stroke="#999" stroke-width="1.6"/></svg>Clean layout for lorem</span>
    <span><svg width="9" height="8" viewBox="0 0 9 8"><path d="M1 4 L3.5 6.5 L8 1" fill="none" stroke="#999" stroke-width="1.6"/></svg>Visually appealing dolor</span>
  </div>
  <div class="abs services-photo" role="img" aria-label="Angler fishing from a small boat on a green lake"></div>
  <svg class="abs connectors" width="80" height="140" viewBox="0 0 80 140">
    <line x1="0" y1="33" x2="65" y2="33" stroke="var(--line)" stroke-width="1"/><circle cx="65" cy="33" r="1.8" fill="var(--line)"/>
    <line x1="0" y1="82" x2="15" y2="82" stroke="var(--line)" stroke-width="1"/><circle cx="15" cy="82" r="1.8" fill="var(--line)"/>
    <line x1="0" y1="131" x2="65" y2="131" stroke="var(--line)" stroke-width="1"/><circle cx="65" cy="131" r="1.8" fill="var(--line)"/>
  </svg>
  <div class="abs thumb" style="left:596px;top:844px;background:linear-gradient(180deg,#c9d8ea 0%,#6e7a5a 40%,#a08560 62%,#5d6c7a 100%)" role="img" aria-label="Riverbank cliff"></div>
  <div class="abs thumb" style="left:546px;top:893px;background:linear-gradient(180deg,#b9c8dc 0%,#7a5e48 35%,#9c7a5a 60%,#4e5560 100%)" role="img" aria-label="Rocky hillside by the water"></div>
  <div class="abs thumb" style="left:596px;top:943px;background:linear-gradient(160deg,#8a6a2e 0%,#c09a4a 45%,#5e4a2a 100%)" role="img" aria-label="Fly shop interior"></div>
</section>

<footer>
  <div class="abs footer"></div>
  <h3 class="abs footer-head" style="left:77px;top:1041px">
    <svg width="19" height="15" viewBox="0 0 18 15"><path d="M1 2 H7 L9 4 H17 V14 H1Z" fill="var(--sky)"/></svg>Links</h3>
  <ul class="abs footer-links">
    <li class="active"><a href="#">Home</a></li>
    <li><a href="#">About Us</a></li>
    <li><a href="#">Guided Trips</a></li>
    <li><a href="#">Fly Shop</a></li>
    <li><a href="#">Missouri River About</a></li>
    <li><a href="#">Contact Us</a></li>
  </ul>
  <h3 class="abs footer-head" style="left:237px;top:1041px">
    <svg width="14" height="14" viewBox="0 0 14 14"><rect y="1" width="14" height="3" rx="1.5" fill="var(--sky)"/><rect y="6" width="14" height="3" rx="1.5" fill="var(--sky)"/><rect y="11" width="14" height="3" rx="1.5" fill="var(--sky)"/></svg>About Us</h3>
  <p class="abs footer-about">Lorem Ipsum is simply dummy text of the printing and typesetting industry. Lorem Ipsum has been the industry's standard dummy text ever since the 1500s,</p>
  <div class="abs socials"><span></span><span></span><span></span><span></span></div>
  <h3 class="abs footer-head" style="left:490px;top:1041px">
    <svg width="12" height="16" viewBox="0 0 12 16"><path d="M6 1 C2.5 1 1 3.5 1 5.5 C1 9 6 15 6 15 C6 15 11 9 11 5.5 C11 3.5 9.5 1 6 1Z" fill="var(--sky)"/><circle cx="6" cy="5.5" r="1.8" fill="var(--footer)"/></svg>Find Us</h3>
  <div class="abs map" role="img" aria-label="Street map showing the shop location"></div>
  <div class="abs footer-base">Copyright 2014 © <b>Larkwell Bend.</b> All Rights Reserved</div>
</footer>

</body>
</html>
```